KRV Construction Management -Business card design request- Lioness black and white shema ONLY - No

It is a woman on construction company I would like the schema to be in black-and-white with the lioness and possibly a lion anulinus as me and my husband both kind of running I would like to see designs for both. Original art would be preferred but like I said I'm going to attach some pictures that I really like and also if you could check my website out that would be great.Please get very creative this is a very important company I will be combining quality construction services with quality construction company and community affiliates such as Halvick construction exedra I really need to show dominates all I'm really wanting is the black-and-white montre and the lioness image on the right side as you will see in some of the thumbnails from what I have had in the past it is OK but I can't connect with anything. These are the last of my advertising dollars I ask that you really please put some time and help me take my company it to the next century. This is going to be a global thing it will be very serious. I'm not trying to be arrogant I'm just trying to tell the truth I ask that you give me something of quality that something that I can put on folders billboards pains walking to places and that it's not that I'm a woman own business but I deftly want there to be A-line as and please play around with the image of the lion and lioness as my husband is a lot of the construction side and I have a decided if Im going to advertise that are notJmsconstructionmanagement.comJovanna Schlossenberg C.E.O.KRV Construction Management Marisela@jmsconstructionmanagement.com81.316.0990

Target Market(s)

Construction or management style. Understand theme ports of marketing and that this logo will be displayed on billboards D cows apps all across the country

Industry/Entity Type

Construction Company

Contact Information for Business Card

Marisela Vandertook
C.E.O.

Marisela@krvconstructionmanagement.example

Www.krvconstructionmanagement.example

729.584.1437

If you can I would like my slogan on their connecting qualify construction services with qualified construction companies and community affiliates

Font styles to use
Sans Serif

Colors
ffffff

Requirements
Must have
• Black-and-white schema lioness on the back side I will list my services will get to that but for now I wanna get the logo design I very open to where you maneuver the contact information
• Marisela Vandertook
• C.E.O.
• Marisela@krvconstructionmanagement.example
• Www.krvconstructionmanagement.example
• 729.584.1437
• If you can I would like my slogan on their connecting qualified construction services with qualified construction companies and community affiliates
Nice to have
• Everything I mentioned above.
• I have added a few pictures with a lion and Linus and know this may seem crazy but I do not like that they are facing to the left I would rather the lion and lioness looked to the right and face forward. Also all the images need to be in black-and-white have provided some color want but I'd like them change to sepia .
Should not have
• I do not want it to look like a cartoon I need this to be of the utmost professionalism

```html
<!DOCTYPE html>
<html lang="en">
<head>
<meta charset="utf-8">
<title>KRV Construction Management — Business Card</title>
<link rel="stylesheet" href="https://fonts.googleapis.com/css2?family=Roboto+Condensed:wght@300;400;700&family=Fira+Sans:ital,wght@1,300&display=swap">
<style>
  :root {
    --paper: #ffffff;
    --frame: #7a7a7a;
    --ink-strong: #2b2b2b;
    --ink: #4a4a4a;
    --ink-soft: #5a5a5a;
    --lion-tone: rgba(115, 115, 115, 0.95);
    --lion-tone-mid: rgba(115, 115, 115, 0.55);
    --lion-tone-fade: rgba(115, 115, 115, 0);
  }
  * { margin: 0; padding: 0; box-sizing: border-box; }
  html, body {
    width: 1200px;
    height: 753px;
    overflow: hidden;
    background: var(--paper);
  }
  .canvas {
    position: relative;
    width: 1200px;
    height: 753px;
    background: var(--paper);
    font-family: "Roboto Condensed", "Arial Narrow", sans-serif;
  }
  .card {
    position: absolute;
    left: 90px;
    top: 76px;
    width: 1021px;
    height: 600px;
    border: 2px solid var(--frame);
    background: var(--paper);
    overflow: hidden;
  }
  .lion-art {
    position: absolute;
    left: 510px;
    top: 18px;
    width: 509px;
    height: 520px;
    background:
      radial-gradient(ellipse 62% 58% at 48% 42%, var(--lion-tone) 0%, var(--lion-tone) 45%, var(--lion-tone-mid) 72%, var(--lion-tone-fade) 100%),
      radial-gradient(ellipse 40% 45% at 100% 72%, var(--lion-tone) 0%, var(--lion-tone-mid) 60%, var(--lion-tone-fade) 100%);
  }
  .brand {
    position: absolute;
    left: 70px;
    top: 100px;
    width: 421px;
    display: flex;
    align-items: center;
    justify-content: flex-end;
    gap: 14px;
  }
  .brand-mark {
    width: 52px;
    height: 52px;
    border-radius: 50%;
    background: #737373;
    flex: none;
  }
  .brand-name {
    font-weight: 700;
    font-size: 29px;
    line-height: 1;
    color: var(--ink-strong);
    white-space: nowrap;
  }
  .contact {
    position: absolute;
    right: 530px;
    text-align: right;
    color: var(--ink);
    font-weight: 300;
    font-style: normal;
    white-space: nowrap;
  }
  .contact-line {
    position: absolute;
    right: 0;
    line-height: 1;
  }
  .address { top: 200px; font-size: 25px; }
  .address .contact-line:nth-child(1) { top: 0; }
  .address .contact-line:nth-child(2) { top: 37px; }
  .address .contact-line:nth-child(3) { top: 75px; }
  .address .contact-line:nth-child(4) { top: 112px; }
  .online { top: 349px; font-size: 21.5px; }
  .online .contact-line:nth-child(1) { top: 0; }
  .online .contact-line:nth-child(2) { top: 31px; }
  .label { margin-right: 6px; }
  .person {
    position: absolute;
    right: 530px;
    top: 454px;
    text-align: right;
    white-space: nowrap;
  }
  .person-name {
    font-weight: 400;
    font-size: 46px;
    letter-spacing: -0.8px;
    line-height: 1;
    color: var(--ink-strong);
  }
  .person-title {
    margin-top: 12px;
    font-weight: 300;
    font-size: 23px;
    letter-spacing: 1px;
    line-height: 1;
    color: var(--ink);
  }
  .slogan {
    position: absolute;
    right: 40px;
    top: 502px;
    text-align: right;
    font-family: "Fira Sans", "Trebuchet MS", sans-serif;
    font-style: italic;
    font-weight: 300;
    font-size: 20.5px;
    line-height: 23.5px;
    color: var(--ink-soft);
    white-space: nowrap;
  }
</style>
</head>
<body>
  <main class="canvas">
    <section class="card">
      <div class="lion-art" role="img" aria-label="Grey illustration of a striding lion with a full mane, filling the right half of the card"></div>

      <header class="brand">
        <span class="brand-mark"></span>
        <span class="brand-name">KRV Construction Management</span>
      </header>

      <address class="contact address">
        <span class="contact-line">Northgate Ventures LLC</span>
        <span class="contact-line">2740 NE 61st St Kansas City,</span>
        <span class="contact-line">MO 64119 US</span>
        <span class="contact-line"><span class="label">Ph:</span> 729.584.1437</span>
      </address>

      <div class="contact online">
        <span class="contact-line"><span class="label">Email:</span> Marisela@krvconstructionmanagement.example</span>
        <span class="contact-line"><span class="label">Website:</span>Www.krvconstructionmanagement.example</span>
      </div>

      <div class="person">
        <p class="person-name">Marisela Vandertook</p>
        <p class="person-title">C.E.O.</p>
      </div>

      <p class="slogan">
        connecting qualify construction<br>
        services with qualified construction<br>
        companies and community affiliates
      </p>
    </section>
  </main>
</body>
</html>
```